Plakat-Design für Werbetafel-Design für Fussballplatz
Zielgruppe
IT Consulting Dienstleistungen für Internationale Kunden
Aufgabenstellung
Werbetafel-Design für Fussballplatz. (Logo in groß + Slogan 'THE CODE STEWARDS')
Format: 3,0 x 0,75 m
Druckdatenvorabe anbei.

```html
<!DOCTYPE html>
<html lang="en">
<head>
<meta charset="utf-8">
<title>VELTRANEX – Stadium Board</title>
<link rel="stylesheet" href="https://fonts.googleapis.com/css2?family=Raleway:wght@400;500&family=Montserrat:ital,wght@1,900&display=swap">
<style>
  :root {
    --stage: #252b2e;
    --board: #ffffff;
    --brand-blue: #2e83c2;
    --brand-green: #6e9e33;
    --ink: #1d1d1b;
    --tint-blue: #d3e5f2;
    --tint-green: #e6efdc;
  }
  * { margin: 0; padding: 0; box-sizing: border-box; }
  html, body {
    width: 1200px; height: 745px; overflow: hidden;
    background: var(--stage);
  }
  .stage { position: relative; width: 1200px; height: 745px; }
  .board {
    position: absolute; left: 58px; width: 1084px; height: 271px;
    background: var(--board); overflow: hidden;
  }
  .board--left-accent { top: 58px; }
  .board--right-accent { top: 416px; }
  .board__backdrop { position: absolute; inset: 0; width: 100%; height: 100%; }

  .brand-mark {
    position: absolute; left: 56px; top: 64px;
    width: 132px; height: 132px; border-radius: 50%;
    background: var(--brand-blue);
  }
  .wordmark {
    position: absolute; left: 294px; top: 84px;
    display: flex; flex-direction: column; align-items: flex-end;
    white-space: nowrap;
  }
  .wordmark__name {
    font-family: "Raleway", sans-serif; font-weight: 400;
    font-size: 74px; line-height: 74px; letter-spacing: -0.5px;
    color: var(--ink);
  }
  .wordmark__tagline {
    margin-top: 8px;
    font-family: "Raleway", sans-serif; font-weight: 500;
    font-size: 32px; line-height: 32px; color: var(--brand-blue);
  }
  .slogan {
    position: absolute; left: 763px; top: 86px;
    font-family: "Montserrat", sans-serif; font-style: italic; font-weight: 900;
    font-size: 42px; line-height: 50px; letter-spacing: 0.3px;
    white-space: nowrap;
  }
  .slogan__top { display: block; color: var(--brand-green); }
  .slogan__bottom { display: block; color: var(--brand-blue); }
</style>
</head>
<body>
<main class="stage">

  <section class="board board--left-accent">
    <svg class="board__backdrop" viewBox="0 0 1084 271" role="img" aria-label="Faint brand pattern in soft blue and green tints">
      <defs>
        <linearGradient id="fadeBlueLeft" x1="0" x2="1">
          <stop offset="0" stop-color="#d3e5f2"/>
          <stop offset="1" stop-color="#d3e5f2" stop-opacity="0"/>
        </linearGradient>
        <linearGradient id="fadeGreenLeft" x1="0" x2="1">
          <stop offset="0" stop-color="#e6efdc"/>
          <stop offset="1" stop-color="#e6efdc" stop-opacity="0"/>
        </linearGradient>
      </defs>
      <rect x="0" y="0" width="360" height="271" fill="url(#fadeBlueLeft)" opacity="0.9"/>
      <rect x="176" y="0" width="340" height="271" fill="url(#fadeGreenLeft)" opacity="0.7"/>
    </svg>
    <span class="brand-mark"></span>
    <div class="wordmark">
      <span class="wordmark__name">VELTRANEX</span>
      <span class="wordmark__tagline">IT Consulting</span>
    </div>
    <p class="slogan"><span class="slogan__top">THE CODE</span><span class="slogan__bottom">STEWARDS</span></p>
  </section>

  <section class="board board--right-accent">
    <svg class="board__backdrop" viewBox="0 0 1084 271" role="img" aria-label="Faint brand pattern in soft blue and green tints">
      <defs>
        <linearGradient id="fadeBlueRight" x1="1" x2="0">
          <stop offset="0" stop-color="#d3e5f2"/>
          <stop offset="1" stop-color="#d3e5f2" stop-opacity="0"/>
        </linearGradient>
        <linearGradient id="fadeGreenRight" x1="1" x2="0">
          <stop offset="0" stop-color="#e6efdc"/>
          <stop offset="1" stop-color="#e6efdc" stop-opacity="0"/>
        </linearGradient>
      </defs>
      <rect x="640" y="0" width="444" height="271" fill="url(#fadeBlueRight)" opacity="0.9"/>
      <rect x="900" y="0" width="184" height="271" fill="url(#fadeGreenRight)" opacity="0.8"/>
    </svg>
    <span class="brand-mark"></span>
    <div class="wordmark">
      <span class="wordmark__name">VELTRANEX</span>
      <span class="wordmark__tagline">IT Consulting</span>
    </div>
    <p class="slogan"><span class="slogan__top">THE CODE</span><span class="slogan__bottom">STEWARDS</span></p>
  </section>

</main>
</body>
</html>
```